Modern Label for cleaning products for the brand Voralux

We need a label design for our line of cleaning products. The label should feature our logo and an image to identify the product's intended use. I've added our logo and an image for use. This only concerns the design of the label on the front of the bottle.

Label dimensions:
Label 1 (500ml bottle with spray): width 58mm x height 115mm
Label 2: (1L bottle): width 73mm x height 140mm
The design must be consistent for both bottles which you find in the pictures.

The bottles to be labeled are white. See the attachment for a photo of the bottles.

The photo must also appear on the label to identify the product's intended use.

Product information:
Brand: Voralux
Product: Sanitary Cleaner

This text must be placed on the label:
"Cleans, descales & freshens. followed with this text: "Ideal for quick and powerful cleaning. A ready-to-use product for everyday use."

- Mention the seperate USP's: Sanitary, Bathroom, Toilet, Wet areas

Appearance: This is a consumer product, but it must have a professional appearance. We would like to see a design that use the color blue from our logo.

Target Market(s)

Consumers who take care of their homes and want to maintain it the correct (professional) way

Font styles to use
Sans Serif

Colors
0054AA
0677BA
7BADD7
CADEEF
E8F1F8

Requirements
Must have
• USP's + use of image and logo + blend in 1 design
Nice to have
• Keep the color of the logo in the design
Should not have
• Comic sans

```html
<!DOCTYPE html>
<html lang="en">
<head>
<meta charset="utf-8">
<title>Voralux Sanitary Cleaner – Labels</title>
<link rel="stylesheet" href="https://fonts.googleapis.com/css2?family=Rubik:wght@400;500;600;700&display=swap">
<style>
  :root {
    --blue-deep: #0054AA;
    --blue-mid: #0677BA;
    --blue-soft: #7BADD7;
    --blue-pale: #CADEEF;
    --blue-mist: #E8F1F8;
    --navy: #0b3c8f;
    --ink: #1b1b1f;
    --usp-red: #c8102e;
    --white: #ffffff;
    --stage: #eeeff1;
  }
  * { box-sizing: border-box; margin: 0; padding: 0; }
  html, body { width: 1200px; height: 909px; overflow: hidden; }
  body {
    background: radial-gradient(ellipse at 50% 40%, #f7f8f9 0%, var(--stage) 70%, #e6e7e9 100%);
    font-family: "Rubik", Arial, sans-serif;
    position: relative;
  }

  /* ---------- label ---------- */
  .label {
    position: absolute;
    background: var(--white);
    overflow: hidden;
    box-shadow: 0 2px 10px rgba(0, 40, 90, 0.12);
  }
  .label--500 { left: 209px; top: 418px; width: 207px; height: 410px; font-size: 10px; }
  .label--1000 { left: 782px; top: 330px; width: 253px; height: 498px; font-size: 12.2px; }

  .label__headline {
    position: absolute; top: 3%; left: 0; right: 0;
    text-align: center;
    color: var(--blue-mid);
    font-weight: 600;
    font-size: 1.45em;
    line-height: 1.2;
    letter-spacing: 0.03em;
    text-transform: uppercase;
  }
  .label__band {
    position: absolute; left: 0; top: 16%;
    width: 100%; height: 84%;
    display: block;
  }
  .label__tagline {
    position: absolute; top: 23.6%; left: 0; right: 0;
    text-align: center;
    color: var(--white);
    font-size: 0.78em;
    letter-spacing: 0.01em;
  }
  .label__photo {
    position: absolute; left: 0; right: 0; bottom: 0; height: 32%;
    background:
      linear-gradient(180deg, rgba(0, 84, 170, 0.85) 0%, rgba(6, 119, 186, 0.25) 30%, rgba(0, 0, 0, 0) 50%),
      linear-gradient(90deg, #8d8f92 0%, #c9cbcd 30%, #e9e9e8 50%, #bdbdbc 75%, #9fa2a5 100%);
  }
  .label__volume {
    position: absolute; bottom: 1.2%; left: 0; right: 0;
    text-align: center;
    color: var(--white);
    font-size: 1.25em;
    font-weight: 500;
  }
  .label__panel {
    position: absolute; left: 12%; right: 12%; top: 26.8%; height: 44%;
    background: radial-gradient(ellipse at 50% 35%, var(--white) 60%, var(--blue-mist) 85%, var(--blue-pale) 100%);
    border-radius: 0 0 50% 50% / 0 0 26% 26%;
    text-align: center;
  }
  .brand {
    position: absolute; top: 19%; left: 0; right: 0;
    display: flex; align-items: center; justify-content: center; gap: 0.35em;
  }
  .brand__dot {
    width: 0.9em; height: 0.9em; border-radius: 50%;
    background: var(--blue-mid);
    font-size: 1.9em;
  }
  .brand__name {
    color: var(--ink);
    font-weight: 600;
    font-size: 1.9em;
    letter-spacing: 0.01em;
  }
  .label__claim {
    position: absolute; top: 50%; left: 0; right: 0;
    color: var(--blue-mid);
    font-weight: 700;
    font-size: 1.3em;
    line-height: 1.25;
    text-transform: uppercase;
  }
  .label__usps {
    position: absolute; top: 81%; left: 0; right: 0;
    color: var(--usp-red);
    font-weight: 500;
    font-size: 0.8em;
    line-height: 1.3;
    text-transform: uppercase;
  }

  /* ---------- centre brand ---------- */
  .centre-brand {
    position: absolute; left: 470px; top: 480px;
    width: 260px;
    display: flex; align-items: center; justify-content: center; gap: 12px;
  }
  .centre-brand__dot { width: 38px; height: 38px; border-radius: 50%; background: var(--blue-mid); }
  .centre-brand__name { color: var(--ink); font-weight: 600; font-size: 44px; letter-spacing: 0.01em; }
</style>
</head>
<body>

<section class="label label--500" aria-label="Voralux Sanitary Cleaner 500ml label">
  <h2 class="label__headline">Cleans,<br>descales<br>&amp; freshens</h2>
  <svg class="label__band" viewBox="0 0 100 100" preserveAspectRatio="none" aria-hidden="true">
    <defs>
      <linearGradient id="band500" x1="0" y1="0" x2="0" y2="1">
        <stop offset="0" stop-color="#0b3c8f"/>
        <stop offset="0.5" stop-color="#0054AA"/>
        <stop offset="1" stop-color="#0677BA"/>
      </linearGradient>
    </defs>
    <path d="M0 2 C25 5 45 4 65 1 C80 -1 92 1 100 3 L100 100 L0 100 Z" fill="url(#band500)"/>
  </svg>
  <p class="label__tagline">A ready-to-use product for everyday use.</p>
  <div class="label__photo" role="img" aria-label="Photo of a modern bathroom with walk-in shower, washbasin and mosaic tiles"></div>
  <div class="label__panel">
    <div class="brand"><span class="brand__dot"></span><span class="brand__name">Voralux</span></div>
    <p class="label__claim">Ideal for quick<br>and powerful<br>cleaning.</p>
    <p class="label__usps">Sanitary, bathroom,<br>toilet, wet areas</p>
  </div>
  <p class="label__volume">500ml</p>
</section>

<div class="centre-brand"><span class="centre-brand__dot"></span><span class="centre-brand__name">Voralux</span></div>

<section class="label label--1000" aria-label="Voralux Sanitary Cleaner 1000 ml label">
  <h2 class="label__headline">Cleans,<br>descales<br>&amp; freshens</h2>
  <svg class="label__band" viewBox="0 0 100 100" preserveAspectRatio="none" aria-hidden="true">
    <defs>
      <linearGradient id="band1000" x1="0" y1="0" x2="0" y2="1">
        <stop offset="0" stop-color="#0b3c8f"/>
        <stop offset="0.5" stop-color="#0054AA"/>
        <stop offset="1" stop-color="#0677BA"/>
      </linearGradient>
    </defs>
    <path d="M0 2 C25 5 45 4 65 1 C80 -1 92 1 100 3 L100 100 L0 100 Z" fill="url(#band1000)"/>
  </svg>
  <p class="label__tagline">A ready-to-use product for everyday use.</p>
  <div class="label__photo" role="img" aria-label="Photo of a modern bathroom with walk-in shower, washbasin and mosaic tiles"></div>
  <div class="label__panel">
    <div class="brand"><span class="brand__dot"></span><span class="brand__name">Voralux</span></div>
    <p class="label__claim">Ideal for quick<br>and powerful<br>cleaning.</p>
    <p class="label__usps">Sanitary, bathroom,<br>toilet, wet areas</p>
  </div>
  <p class="label__volume">1000 ml</p>
</section>

</body>
</html>
```